Communication and Marketing agency needs a new presentation card

We are a group of communication and marketing agencies specialized in companies that are in the logistics and industrial sector. The head agency is TELVANO Grupo and the group consists of 4 agencies: TELVANO Media, TELVANO Digital, TELVANO Research and EnlazaPorImagen. We hace 4 offices in Spain (Madrid, Barcelona, Valencia and Murcia). We are looking for a clean and attractive design that transmits our experience, brand presence in the market and knowledge to those who receive the card.It has to maintain the colors of the logo that is attached.
Target Market(s)
logistics and industrial sector
Marketing department
Clean and attractive design

```html
<!DOCTYPE html>
<html lang="en">
<head>
<meta charset="utf-8">
<title>TELVANO Grupo – Business Card</title>
<link href="https://fonts.googleapis.com/css2?family=Roboto:wght@400;500&family=Roboto+Condensed:wght@500;700&display=swap" rel="stylesheet">
<style>
  :root{
    --bg:#d9d9d9;
    --card:#ffffff;
    --red:#c8102e;
    --ink:#3a3a3a;
    --grey:#5d5a58;
    --rule:#8a8a8a;
  }
  *{box-sizing:border-box;margin:0;padding:0}
  html,body{width:1200px;height:951px;overflow:hidden;background:var(--bg)}
  body{position:relative;font-family:"Roboto",sans-serif;color:var(--ink)}
  .card{position:absolute;top:321px;width:540px;height:309px;background:var(--card);
        box-shadow:0 10px 30px rgba(0,0,0,.18)}
  .card--front{left:40px}
  .card--back{left:620px}

  /* front */
  .person{position:absolute;left:34px;top:70px}
  .person__name{font-family:"Roboto Condensed",sans-serif;font-weight:700;font-size:27px;color:var(--ink);letter-spacing:.3px}
  .person__name span{color:var(--red)}
  .person__role{font-size:13px;color:var(--ink);margin-top:2px;letter-spacing:.4px}
  .divider{position:absolute;left:34px;right:0;top:138px;height:1px;background:var(--rule)}
  .contacts{position:absolute;left:34px;top:152px;list-style:none}
  .contacts li{display:flex;align-items:center;gap:10px;font-size:13px;line-height:21px;letter-spacing:.3px}
  .contacts svg{width:10px;height:10px;fill:var(--red);flex:none}
  .address{position:absolute;right:34px;top:152px;text-align:left;font-size:14px;line-height:20px;letter-spacing:.4px}
  .brand{position:absolute;font-family:"Roboto Condensed",sans-serif;font-weight:500;color:var(--red);letter-spacing:2px;white-space:nowrap}
  .card--front .brand{right:40px;top:60px;font-size:30px}

  /* back */
  .card--back .brand--main{left:0;right:0;top:88px;text-align:center;font-size:40px;letter-spacing:4px}
  .back-rule{position:absolute;left:0;right:0;top:176px;height:1px;background:var(--red)}
  .agencies{position:absolute;left:14px;right:14px;top:188px;display:flex;justify-content:space-between;list-style:none}
  .agencies li{font-family:"Roboto Condensed",sans-serif;font-weight:500;font-size:13px;letter-spacing:.8px;color:var(--red)}
  .agencies li.is-grey{color:var(--grey)}
  .offices{position:absolute;left:0;right:0;top:232px;height:22px;background:var(--grey);
           color:#fff;font-size:12px;line-height:22px;text-align:center;letter-spacing:1px}
</style>
</head>
<body>

<section class="card card--front" aria-label="Business card front">
  <div class="person">
    <h1 class="person__name">Tomás <span>Ferrer</span></h1>
    <p class="person__role">Founder &amp; CEO</p>
  </div>
  <div class="brand">TELVANO Grupo</div>
  <div class="divider"></div>
  <ul class="contacts">
    <li><svg viewBox="0 0 10 10"><rect x="2.5" y="0" width="5" height="10" rx="1"/></svg>555 014 2290</li>
    <li><svg viewBox="0 0 10 10"><path d="M2 0l2 2.5-1.2 1.2a6 6 0 003.5 3.5L7.5 6 10 8l-1.5 2C4 10 0 6 0 1.5z"/></svg>555 203 8841</li>
    <li><svg viewBox="0 0 10 10"><path d="M0 2h10v6H0z M0 2l5 3.5L10 2" /></svg>hola@telvanogrupo.es</li>
    <li><svg viewBox="0 0 10 10"><circle cx="5" cy="5" r="5"/></svg>www.telvanogrupo.es</li>
  </ul>
  <address class="address" style="font-style:normal">4120 N. Harlow PKWY Ste. B<br>Linden, TX 60412</address>
</section>

<section class="card card--back" aria-label="Business card back">
  <div class="brand brand--main">TELVANO Grupo</div>
  <div class="back-rule"></div>
  <ul class="agencies">
    <li>TELVANO Media</li>
    <li class="is-grey">TELVANO Digital</li>
    <li class="is-grey">TELVANO Research</li>
    <li>EnlazaPorImagen</li>
  </ul>
  <div class="offices">Madrid | Barcelona | Valencia | Murcia</div>
</section>

</body>
</html>
```